Ridgeline Outfitters Business Cards

Recently had a logo done with Artfolio and now looking for a business card to go along with it.

Target Market(s)

Ridgeline Outfitters is a weapons dealer. My market will be primarily men, hunting, shooting type.

Industry/Entity Type

Business

Contact Information for Business Card

I selected double sided, but this is not required, single or double is going to be fine. I picture the logo on one side, or perhaps just the circle which contains "RO" with the remaining info on the other side.

Font styles to use
Sans Serif

Requirements
Must have
• My name: Milo Brandt
• Title: Owner
• tel: 612-555-0187
• web: www.ridgelineoutfittersmn.example
Nice to have
• I like the concept of a black business card. I would like to keep the colors monotone, black, grey, white or red. Red is acceptable because it is in the logo. I have also seen cards that are matte black with shiny black as well, perhaps for the logo (or circle RO) part of the logo.
• I will upload a couple of the logos for use, and also an example I just found of the black on black. and some others that have a nice contrast.
Should not have
• lots of colors are not wanted.

```html
<!DOCTYPE html>
<html lang="en">
<head>
<meta charset="utf-8">
<title>Ridgeline Outfitters Business Cards</title>
<link href="https://fonts.googleapis.com/css2?family=Exo+2:wght@400;600;700&display=swap" rel="stylesheet">
<style>
  :root {
    --stage: #2b2b2b;
    --card: #050505;
    --gloss: #151515;
    --gloss-edge: #2a2a2a;
    --red: #e3202b;
    --grey: #8a8a8a;
    --grey-light: #b5b5b5;
    --rule: #5a5a5a;
  }
  * { box-sizing: border-box; margin: 0; padding: 0; }
  html, body { width: 1200px; height: 900px; overflow: hidden; }
  body {
    background: var(--stage);
    font-family: "Exo 2", sans-serif;
    display: flex;
    flex-direction: column;
    align-items: center;
    justify-content: center;
    gap: 56px;
  }
  .card {
    position: relative;
    width: 600px;
    height: 343px;
    background: var(--card);
    overflow: hidden;
    box-shadow: 0 18px 40px rgba(0,0,0,.55);
  }
  /* front */
  .front-seal {
    position: absolute;
    left: 300px;
    top: -6px;
    width: 290px;
    height: 290px;
  }
  .front-brand {
    position: absolute;
    left: 34px;
    bottom: 40px;
  }
  .brand-name {
    color: var(--red);
    font-weight: 700;
    text-transform: uppercase;
    letter-spacing: 1px;
    line-height: 1;
  }
  .front-brand .brand-name { font-size: 27px; }
  .brand-rule {
    height: 1px;
    background: var(--rule);
    margin-top: 8px;
  }
  /* back */
  .back-brand {
    position: absolute;
    left: 34px;
    top: 40px;
    display: flex;
    align-items: center;
    gap: 12px;
  }
  .brand-dot {
    width: 46px;
    height: 46px;
    border-radius: 50%;
    border: 3px solid var(--grey);
  }
  .back-brand .brand-name { font-size: 18px; }
  .contact {
    position: absolute;
    left: 40px;
    bottom: 34px;
    color: var(--grey);
  }
  .person-name {
    font-size: 20px;
    font-weight: 700;
    color: var(--grey);
    letter-spacing: .5px;
  }
  .person-rule {
    width: 200px;
    height: 1px;
    background: var(--rule);
    margin: 6px 0 4px;
  }
  .person-title { font-size: 14px; margin-bottom: 12px; }
  .contact-line {
    display: flex;
    align-items: center;
    gap: 8px;
    font-size: 15px;
    color: var(--grey-light);
    margin-top: 4px;
  }
  .contact-line svg { width: 13px; height: 13px; flex: none; }
</style>
</head>
<body>
  <section class="card card-front">
    <svg class="front-seal" viewBox="0 0 290 290" aria-hidden="true">
      <circle cx="145" cy="145" r="138" fill="var(--gloss)" stroke="var(--gloss-edge)" stroke-width="3"/>
    </svg>
    <div class="front-brand">
      <div class="brand-name">Ridgeline Outfitters</div>
      <div class="brand-rule"></div>
    </div>
  </section>

  <section class="card card-back">
    <div class="back-brand">
      <span class="brand-dot"></span>
      <div>
        <div class="brand-name">Ridgeline Outfitters</div>
        <div class="brand-rule"></div>
      </div>
    </div>
    <div class="contact">
      <div class="person-name">Milo Brandt</div>
      <div class="person-rule"></div>
      <div class="person-title">Owner</div>
      <div class="contact-line">
        <svg viewBox="0 0 24 24" aria-hidden="true"><path fill="var(--red)" d="M6.6 10.8a15.1 15.1 0 0 0 6.6 6.6l2.2-2.2a1 1 0 0 1 1-.25 11.4 11.4 0 0 0 3.6.57 1 1 0 0 1 1 1V20a1 1 0 0 1-1 1A17 17 0 0 1 3 4a1 1 0 0 1 1-1h3.5a1 1 0 0 1 1 1c0 1.25.2 2.45.57 3.57a1 1 0 0 1-.25 1z"/></svg>
        <span>612-555-0187</span>
      </div>
      <div class="contact-line">
        <svg viewBox="0 0 24 24" aria-hidden="true"><g fill="none" stroke="var(--red)" stroke-width="2.4"><circle cx="12" cy="12" r="10"/><path d="M2 12h20M12 2c3 3 3 17 0 20M12 2c-3 3-3 17 0 20"/></g></svg>
        <span>www.ridgelineoutfittersmn.example</span>
      </div>
    </div>
  </section>
</body>
</html>
```